Contemporary update for a market leader in foodservice distribution

KORVELT is a market leader in foodservice distribution nationwide.
We have recently adopted a new look and feel for our flagship foodservice rewards programme, and we're looking to have our business cards reflect our new aesthetic. Below is a link to our new rewards website to give you a general idea on the look we're after. https://korveltperks.com.au/

Industry/Entity Type

Distribution

Contact Information for Business Card

Must have space for contact name, position, company name and ABN, address, phone number and direct number, fax, email, and web address.

Font styles to use
Serif
Sans Serif

Requirements
Must have
• We'd like a landscape design, with our 'Tip of the Peak' logo incorporated on either the front or the back of the card. The overall design should be contemporary and professional.
Nice to have
• I have included both the full colour and white version of our company logo - our preference is to have the company logo one solid colour (white, or a shade of grey) although we're also open to designs including the full colour logo. If you are able to incorporate a small Facebook and LinkedIn logo, please do so.
Should not have
• Should not have an over-complicated design. No images of globes, or food.

```html
<!DOCTYPE html>
<html lang="en">
<head>
<meta charset="utf-8">
<title>KORVELT Business Card</title>
<link rel="stylesheet" href="https://fonts.googleapis.com/css2?family=Cinzel:wght@400&family=Lato:wght@400;700;900&display=swap">
<style>
  :root {
    --page: #e9e9e7;
    --card: #2d2f32;
    --card-deep: #232527;
    --photo-light: #8a8b8c;
    --photo-mid: #4b4d50;
    --green: #17a980;
    --white: #ffffff;
    --grey-text: #c9cacc;
    --muted: #9a9c9f;
  }
  * { box-sizing: border-box; margin: 0; padding: 0; }
  html, body { width: 1200px; height: 900px; overflow: hidden; }
  body {
    background: var(--page);
    font-family: "Lato", sans-serif;
    display: flex;
    flex-direction: column;
    align-items: center;
    justify-content: center;
    gap: 36px;
  }
  .card {
    position: relative;
    width: 700px;
    height: 400px;
    background: var(--card);
    overflow: hidden;
    box-shadow: 0 6px 18px rgba(0,0,0,0.18);
  }
  /* Front */
  .front-photo {
    position: absolute;
    left: 0; top: 0;
    width: 360px; height: 100%;
    background: linear-gradient(90deg, var(--photo-light) 0%, var(--photo-mid) 55%, var(--card) 100%);
  }
  .brand {
    position: absolute;
    left: 32px; top: 70px;
    display: flex;
    align-items: center;
    gap: 14px;
    color: var(--white);
  }
  .brand-dot {
    width: 40px; height: 40px;
    border-radius: 50%;
    background: var(--white);
  }
  .brand-name {
    font-family: "Cinzel", serif;
    font-size: 46px;
    letter-spacing: 2px;
    line-height: 1;
  }
  .brand-sub {
    font-size: 9px;
    letter-spacing: 1.6px;
    text-transform: uppercase;
    margin-top: 6px;
  }
  .brand-abn {
    font-size: 9px;
    letter-spacing: 1.4px;
    margin-top: 3px;
    text-align: right;
  }
  .person {
    position: absolute;
    right: 70px; top: 48px;
    text-align: right;
  }
  .person-name {
    font-size: 24px;
    font-weight: 700;
    letter-spacing: 1.5px;
    color: var(--grey-text);
    text-transform: uppercase;
  }
  .person-role {
    font-size: 13px;
    color: var(--muted);
    letter-spacing: 0.5px;
    margin-top: 2px;
  }
  .person-bar {
    position: absolute;
    right: 40px; top: 44px;
    width: 14px; height: 40px;
    background: var(--green);
  }
  .contact-band {
    position: absolute;
    left: 0; right: 40px; bottom: 70px;
    height: 62px;
    background: var(--green);
    display: flex;
    align-items: center;
    justify-content: space-between;
    padding: 0 34px 0 40px;
    color: var(--white);
  }
  .contact-item {
    display: flex;
    align-items: center;
    gap: 12px;
    font-size: 13px;
    line-height: 1.3;
  }
  .contact-item svg { width: 20px; height: 20px; flex: none; }
  /* Back */
  .back { background: radial-gradient(circle at 50% 45%, var(--card) 0%, var(--card-deep) 100%); }
  .reward {
    position: absolute;
    inset: 0;
    display: flex;
    flex-direction: column;
    align-items: center;
    justify-content: center;
    color: var(--white);
  }
  .reward-name {
    font-size: 96px;
    font-weight: 900;
    letter-spacing: 2px;
    line-height: 1;
  }
  .reward-sub {
    font-size: 14px;
    font-weight: 700;
    letter-spacing: 4px;
    margin-top: 10px;
  }
  .social {
    display: flex;
    gap: 10px;
    margin-top: 18px;
  }
  .social span {
    width: 18px; height: 18px;
    border-radius: 50%;
    background: #3a78c9;
  }
</style>
</head>
<body>
  <section class="card front">
    <div class="front-photo" role="img" aria-label="Greyscale photo of a foodservice warehouse with stacked goods"></div>
    <div class="brand">
      <div class="brand-dot"></div>
      <div>
        <div class="brand-name">KORVELT</div>
        <div class="brand-sub">Australian Foodservice Distribution</div>
        <div class="brand-abn">ABN 654321</div>
      </div>
    </div>
    <div class="person">
      <div class="person-name">Marcus Holloway</div>
      <div class="person-role">Managing Director</div>
    </div>
    <div class="person-bar"></div>
    <div class="contact-band">
      <div class="contact-item">
        <svg viewBox="0 0 20 20" aria-hidden="true"><path d="M10 2 1 10h3v8h5v-5h2v5h5v-8h3z" fill="#fff"/></svg>
        <div>88 Tanner Lane,<br>Geelong VIC 3220</div>
      </div>
      <div class="contact-item">
        <svg viewBox="0 0 20 20" aria-hidden="true"><path d="M5 2l3 4-2 2c1 2 3 4 5 5l2-2 4 3-2 3C8 17 3 12 2 5z" fill="#fff"/></svg>
        <div>555 204 7719<br>555 381 0642</div>
      </div>
      <div class="contact-item">
        <svg viewBox="0 0 20 20" aria-hidden="true" fill="none" stroke="#fff" stroke-width="1.5"><circle cx="10" cy="10" r="8"/><ellipse cx="10" cy="10" rx="3.5" ry="8"/><path d="M2 10h16M3.5 6h13M3.5 14h13"/></svg>
        <div>contact@korvelt.com<br>www.korvelt.com</div>
      </div>
    </div>
  </section>

  <section class="card back">
    <div class="reward">
      <div class="reward-name">PEAK</div>
      <div class="reward-sub">FOODSERVICE REWARDS</div>
      <div class="social"><span></span><span></span></div>
    </div>
  </section>
</body>
</html>
```